" Empresa focada em seguros pessoais, tais como seguro saúde, vida, previdência e odontológico, oferecendo segurança e agilidade na contrataçao e manutençao e também qualidade de vida. "

```html
<!DOCTYPE html>
<html lang="pt-BR">
<head>
<meta charset="UTF-8">
<title>CelesteVida – Envelope Carta</title>
<link rel="stylesheet" href="https://fonts.googleapis.com/css2?family=Montserrat:wght@400;600&display=swap">
<style>
  :root {
    --backdrop: #eceff2;
    --navy: #1b3a7e;
    --cyan: #0fbcd4;
    --paper: #ffffff;
  }
  html, body {
    margin: 0;
    padding: 0;
    overflow: hidden;
  }
  .canvas {
    position: relative;
    width: 1200px;
    height: 1200px;
    background: var(--backdrop);
    overflow: hidden;
    font-family: "Montserrat", Arial, sans-serif;
  }
  .envelope-die {
    position: absolute;
    inset: 0;
  }
  .flap-top { fill: var(--navy); }
  .envelope-body { fill: var(--paper); }
  .flap-bottom { fill: var(--cyan); }

  .front-brand {
    position: absolute;
    left: 276px;
    top: 352px;
    display: flex;
    align-items: center;
    gap: 14px;
  }
  .brand-dot {
    width: 44px;
    height: 44px;
    border-radius: 50%;
    background: var(--cyan);
    flex: none;
  }
  .brand-name {
    margin: 0;
    font-size: 44px;
    font-weight: 600;
    line-height: 1;
    color: var(--navy);
    letter-spacing: -0.5px;
    white-space: nowrap;
  }
  .brand-tagline {
    margin: 6px 0 0;
    font-size: 13px;
    font-weight: 400;
    color: var(--cyan);
    letter-spacing: 0.5px;
    white-space: nowrap;
  }

  .back-flap {
    position: absolute;
    left: 390px;
    top: 716px;
    width: 470px;
    height: 80px;
    display: flex;
    align-items: center;
    justify-content: space-between;
    transform: rotate(180deg);
    color: var(--paper);
  }
  .back-brand {
    display: flex;
    align-items: center;
    gap: 8px;
    padding-left: 18px;
    border-left: 2px solid var(--paper);
  }
  .back-brand .brand-dot {
    width: 20px;
    height: 20px;
    background: var(--paper);
  }
  .back-brand .brand-name {
    font-size: 24px;
    color: var(--paper);
  }
  .back-contact {
    margin: 0;
    font-style: normal;
    font-size: 11px;
    line-height: 1.45;
    white-space: nowrap;
  }
</style>
</head>
<body>
<main class="canvas">
  <svg class="envelope-die" width="1200" height="1200" viewBox="0 0 1200 1200" aria-hidden="true">
    <path class="flap-top" d="M180,290 C200,250 210,214 250,212 L962,212 C1002,214 1012,250 1032,290 Z"/>
    <rect class="envelope-body" x="180" y="288" width="852" height="410"/>
    <path class="flap-bottom" d="M180,696 L1032,696 L1004,1000 Q998,1068 936,1058 Q606,1002 276,1058 Q214,1068 208,1000 Z"/>
  </svg>

  <header class="front-brand">
    <span class="brand-dot"></span>
    <div>
      <h1 class="brand-name">CelesteVida</h1>
      <p class="brand-tagline">Consultoria de Benefícios</p>
    </div>
  </header>

  <section class="back-flap">
    <div class="back-brand">
      <span class="brand-dot"></span>
      <span class="brand-name">CelesteVida</span>
    </div>
    <address class="back-contact">
      Rua das Palmeiras, 120<br>
      (11) 3214-5870<br>
      (11) 3214-5871<br>
      contato@celestevida.com<br>
      www.celestevida.com.br
    </address>
  </section>
</main>
</body>
</html>
```